Memento Mori Calendar

I’m looking for a graphic designer to create a Memento Mori–style life calendar that captures the essence of OLTRAVEN — minimal, timeless, and deeply philosophical.

The design should be black and white only, with a refined, clean aesthetic and a sense of stillness and precision.
It should feel modern yet eternal, reflecting the themes of time, mortality, and presence.

Deliverables (Print-Ready Files):

24 x 30 in

24 x 32 in

24 x 36 in

A1 (594 x 841 mm)

All formats should be high-resolution and ready for professional printing (300 DPI, CMYK).

Design Requirements:

The calendar layout should follow the Memento Mori life calendar concept (weeks of life represented as small squares or circles).

The overall tone: minimal, meditative, monochrome.

Include the brand name: OLTRAVEN (in an elegant, understated placement).

Add the following quote at the bottom or in a subtle position:

“Life can only be understood backwards; but it must be lived forwards.”
— Halvard Lindqvist

Target Market(s)

The OLTRAVEN audience consists of urban, creative individuals aged 25 to 45, belonging to a middle to upper-middle income class. They lead conscious, quietly ambitious lives, seeking balance between inner depth and modern design. Their values center on awareness, presence, authenticity, and emotional depth, reflected in their preference for a monochrome, minimal, and timeless aesthetic. They tend to be introverted, reflective, and spiritually curious, drawn to brands that embody meaning and restraint rather than excess. Their cultural and stylistic affinities include Quillo, Brelk, Ma Tove, The Hall of Quiet, Dorsant, and Valrène — labels that share OLTRAVENs devotion to simplicity, substance, and subtle ritual.

Font styles to use
Serif
Sans Serif

Colors

Designer to choose only greyscale colors for use in the design.

Requirements
Must have
• The calendar layout should follow the Memento Mori life calendar concept (weeks of life represented as small squares or circles). The overall tone: minimal, meditative, monochrome. Include the brand name: grvsolace (in an elegant, understated placement). Add the following quote at the bottom or in a subtle position: “Life can only be understood backwards; but it must be lived forwards.” — Halvard Lindqvist

```html
<!DOCTYPE html>
<html lang="en">
<head>
<meta charset="utf-8">
<title>Memento Mori Life Calendar — Oltraven</title>
<link rel="stylesheet" href="https://fonts.googleapis.com/css2?family=Cinzel:wght@600&family=Crimson+Pro:ital,wght@1,400;1,700&family=Montserrat:wght@500;700&display=swap">
<style>
  :root {
    --backdrop: #b3b3b3;
    --paper: #ffffff;
    --ink: #111111;
    --rule: #555555;
  }
  html, body {
    margin: 0;
    padding: 0;
    width: 907px;
    height: 1200px;
    overflow: hidden;
    background: var(--backdrop);
  }
  .poster {
    position: relative;
    width: 907px;
    height: 1200px;
  }
  .poster svg { display: block; }
  .brand-name {
    font-family: "Montserrat", sans-serif;
    font-weight: 500;
    font-size: 22px;
    letter-spacing: 9px;
    fill: var(--ink);
  }
  .title {
    font-family: "Cinzel", serif;
    font-weight: 600;
    font-size: 50px;
    letter-spacing: 1px;
    fill: var(--ink);
  }
  .num {
    font-family: "Montserrat", sans-serif;
    font-weight: 500;
    font-size: 4.6px;
    fill: var(--ink);
  }
  .num-major {
    font-family: "Montserrat", sans-serif;
    font-weight: 700;
    font-size: 8.5px;
    fill: var(--ink);
  }
  .row-major {
    font-family: "Montserrat", sans-serif;
    font-weight: 700;
    font-size: 10px;
    fill: var(--ink);
  }
  .quote {
    font-family: "Crimson Pro", serif;
    font-style: italic;
    font-weight: 400;
    font-size: 13.5px;
    fill: var(--ink);
  }
  .quote-author {
    font-family: "Crimson Pro", serif;
    font-style: italic;
    font-weight: 700;
    font-size: 13.5px;
    fill: var(--ink);
  }
  .week-box { fill: none; stroke: var(--ink); stroke-width: 0.75; }
</style>
</head>
<body>
<main class="poster">
<svg width="907" height="1200" viewBox="0 0 907 1200" xmlns="http://www.w3.org/2000/svg">
  <defs>
    <pattern id="week" x="0" y="0" width="11.1" height="11.1" patternUnits="userSpaceOnUse">
      <rect class="week-box" x="0.9" y="1" width="8.6" height="8.8" rx="1.8"/>
    </pattern>
    <g id="decade-block">
      <rect width="288.6" height="111" fill="url(#week)"/>
    </g>
    <g id="col-labels-left">
      <text x="0" class="num">1</text><text x="11.1" class="num">2</text><text x="22.2" class="num">3</text><text x="33.3" class="num">4</text><text x="44.4" class="num-major">5</text>
      <text x="55.5" class="num">6</text><text x="66.6" class="num">7</text><text x="77.7" class="num">8</text><text x="88.8" class="num">9</text><text x="99.9" class="num-major">10</text>
      <text x="111" class="num">11</text><text x="122.1" class="num">12</text><text x="133.2" class="num">13</text><text x="144.3" class="num">14</text><text x="155.4" class="num-major">15</text>
      <text x="166.5" class="num">16</text><text x="177.6" class="num">17</text><text x="188.7" class="num">18</text><text x="199.8" class="num">19</text><text x="210.9" class="num-major">20</text>
      <text x="222" class="num">21</text><text x="233.1" class="num">22</text><text x="244.2" class="num">23</text><text x="255.3" class="num">24</text><text x="266.4" class="num-major">25</text>
      <text x="277.5" class="num">26</text>
    </g>
    <g id="col-labels-right">
      <text x="0" class="num">27</text><text x="11.1" class="num">28</text><text x="22.2" class="num">29</text><text x="33.3" class="num-major">30</text><text x="44.4" class="num">31</text>
      <text x="55.5" class="num">32</text><text x="66.6" class="num">33</text><text x="77.7" class="num">34</text><text x="88.8" class="num-major">35</text><text x="99.9" class="num">36</text>
      <text x="111" class="num">37</text><text x="122.1" class="num">38</text><text x="133.2" class="num">39</text><text x="144.3" class="num-major">40</text><text x="155.4" class="num">41</text>
      <text x="166.5" class="num">42</text><text x="177.6" class="num">43</text><text x="188.7" class="num">44</text><text x="199.8" class="num-major">45</text><text x="210.9" class="num">46</text>
      <text x="222" class="num">47</text><text x="233.1" class="num">48</text><text x="244.2" class="num">49</text><text x="255.3" class="num-major">50</text><text x="266.4" class="num">51</text>
      <text x="277.5" class="num">52</text>
    </g>
  </defs>

  <!-- Frame -->
  <rect class="paper" x="56" y="48" width="795" height="1104" rx="4" fill="var(--paper)" stroke="var(--ink)" stroke-width="4"/>

  <!-- Brand name -->
  <text class="brand-name" x="458" y="96" text-anchor="middle">OLTRAVEN</text>

  <!-- Column labels -->
  <g class="col-labels" text-anchor="middle">
    <use href="#col-labels-left" transform="translate(136.2 139)"/>
    <use href="#col-labels-right" transform="translate(510.2 139)"/>
  </g>

  <!-- Week grid: 8 decades × 10 years × 52 weeks -->
  <g class="week-grid">
    <g transform="translate(131.7 142)"><use href="#decade-block"/><use href="#decade-block" x="374"/>
      <g text-anchor="end"><text x="-5" y="8" class="num">1</text><text x="-5" y="19.1" class="num">2</text><text x="-5" y="30.2" class="num">3</text><text x="-5" y="41.3" class="num">4</text><text x="-5" y="52.4" class="num">5</text><text x="-5" y="63.5" class="num">6</text><text x="-5" y="74.6" class="num">7</text><text x="-5" y="85.7" class="num">8</text><text x="-5" y="96.8" class="num">9</text><text x="-3" y="109.5" class="row-major">10</text></g></g>
    <g transform="translate(131.7 261.3)"><use href="#decade-block"/><use href="#decade-block" x="374"/>
      <g text-anchor="end"><text x="-5" y="8" class="num">11</text><text x="-5" y="19.1" class="num">12</text><text x="-5" y="30.2" class="num">13</text><text x="-5" y="41.3" class="num">14</text><text x="-5" y="52.4" class="num">15</text><text x="-5" y="63.5" class="num">16</text><text x="-5" y="74.6" class="num">17</text><text x="-5" y="85.7" class="num">18</text><text x="-5" y="96.8" class="num">19</text><text x="-3" y="109.5" class="row-major">20</text></g></g>
    <g transform="translate(131.7 380.6)"><use href="#decade-block"/><use href="#decade-block" x="374"/>
      <g text-anchor="end"><text x="-5" y="8" class="num">21</text><text x="-5" y="19.1" class="num">22</text><text x="-5" y="30.2" class="num">23</text><text x="-5" y="41.3" class="num">24</text><text x="-5" y="52.4" class="num">25</text><text x="-5" y="63.5" class="num">26</text><text x="-5" y="74.6" class="num">27</text><text x="-5" y="85.7" class="num">28</text><text x="-5" y="96.8" class="num">29</text><text x="-3" y="109.5" class="row-major">30</text></g></g>
    <g transform="translate(131.7 499.9)"><use href="#decade-block"/><use href="#decade-block" x="374"/>
      <g text-anchor="end"><text x="-5" y="8" class="num">31</text><text x="-5" y="19.1" class="num">32</text><text x="-5" y="30.2" class="num">33</text><text x="-5" y="41.3" class="num">34</text><text x="-5" y="52.4" class="num">35</text><text x="-5" y="63.5" class="num">36</text><text x="-5" y="74.6" class="num">37</text><text x="-5" y="85.7" class="num">38</text><text x="-5" y="96.8" class="num">39</text><text x="-3" y="109.5" class="row-major">40</text></g></g>
    <g transform="translate(131.7 619.2)"><use href="#decade-block"/><use href="#decade-block" x="374"/>
      <g text-anchor="end"><text x="-5" y="8" class="num">41</text><text x="-5" y="19.1" class="num">42</text><text x="-5" y="30.2" class="num">43</text><text x="-5" y="41.3" class="num">44</text><text x="-5" y="52.4" class="num">45</text><text x="-5" y="63.5" class="num">46</text><text x="-5" y="74.6" class="num">47</text><text x="-5" y="85.7" class="num">48</text><text x="-5" y="96.8" class="num">49</text><text x="-3" y="109.5" class="row-major">50</text></g></g>
    <g transform="translate(131.7 738.5)"><use href="#decade-block"/><use href="#decade-block" x="374"/>
      <g text-anchor="end"><text x="-5" y="8" class="num">51</text><text x="-5" y="19.1" class="num">52</text><text x="-5" y="30.2" class="num">53</text><text x="-5" y="41.3" class="num">54</text><text x="-5" y="52.4" class="num">55</text><text x="-5" y="63.5" class="num">56</text><text x="-5" y="74.6" class="num">57</text><text x="-5" y="85.7" class="num">58</text><text x="-5" y="96.8" class="num">59</text><text x="-3" y="109.5" class="row-major">60</text></g></g>
    <g transform="translate(131.7 857.8)"><use href="#decade-block"/><use href="#decade-block" x="374"/>
      <g text-anchor="end"><text x="-5" y="8" class="num">61</text><text x="-5" y="19.1" class="num">62</text><text x="-5" y="30.2" class="num">63</text><text x="-5" y="41.3" class="num">64</text><text x="-5" y="52.4" class="num">65</text><text x="-5" y="63.5" class="num">66</text><text x="-5" y="74.6" class="num">67</text><text x="-5" y="85.7" class="num">68</text><text x="-5" y="96.8" class="num">69</text><text x="-3" y="109.5" class="row-major">70</text></g></g>
    <g transform="translate(131.7 977.1)"><use href="#decade-block"/><use href="#decade-block" x="374"/>
      <g text-anchor="end"><text x="-5" y="8" class="num">71</text><text x="-5" y="19.1" class="num">72</text><text x="-5" y="30.2" class="num">73</text><text x="-5" y="41.3" class="num">74</text><text x="-5" y="52.4" class="num">75</text><text x="-5" y="63.5" class="num">76</text><text x="-5" y="74.6" class="num">77</text><text x="-5" y="85.7" class="num">78</text><text x="-5" y="96.8" class="num">79</text><text x="-3" y="109.5" class="row-major">80</text></g></g>
  </g>

  <!-- Central title with tapering rules -->
  <g class="title-column">
    <polygon points="456.6,149 457.9,149 458.4,321 456.1,321" fill="var(--rule)"/>
    <line x1="451" y1="321" x2="463" y2="321" stroke="var(--rule)" stroke-width="0.8"/>
    <text class="title" transform="translate(440 612) rotate(90)" text-anchor="middle">MOMENTO MORI</text>
    <line x1="451" y1="894" x2="463" y2="894" stroke="var(--rule)" stroke-width="0.8"/>
    <polygon points="456.1,894 458.4,894 457.9,1082 456.6,1082" fill="var(--rule)"/>
  </g>

  <!-- Quote -->
  <text class="quote" x="453.5" y="1111" text-anchor="middle">“Life can only be understood backwards; but it must be lived forwards.”</text>
  <text class="quote-author" x="453.5" y="1129" text-anchor="middle">Halvard Lindqvist</text>
</svg>
</main>
</body>
</html>
```